Family business needs stationery redesign with new logo

Family owned company, established in 1987 wanting a brand 'refresh'. We are an electrical, refrigeration and construction company based in the Barkly Region Northern Territory, Australia. We have a new logo we would like to use which is uploaded along with our current letterhead and email signature. We are also dropping the word 'contractors' so please do not include this on any designs. Please note also, the 'orange' color used in our logo and designs should be Northern Territory red ochre which is as follows:

RGB (Hex): #C75B12
PantoneĀ® 159 C
CMYK: 1 / 74 / 100 / 7

We are needing our stationery redesigned using our new logo. Please include letterheads, business cards, envelopes, and email signatures.

We currently use our business letterheads for quotations, invoices, letters, HR matters, and internal memos.

We also need a separate simplified letterhead for internal paperwork such as employee leave forms, meeting agendas, and meeting minutes etc.
Updates

Reason: Needing more submissions of full package designs. We are wanting all our stationery, including business cards, letterheads, email signatures, envelopes, etc to be cohesive. We also require ALL the information, as supplied on our template letterhead, to be included on the new letterhead designs. including electrical license no.etc Thank you, K&W

Reason: needing more time as work has got in the way of looking over designs. A lot of designs not meeting the brief/criteria.

Industry/Entity Type

Business

Colors
0355a3
f37122

Requirements
Must have
• The 'orange' color used in the designs should be Northern Territory red ochre which is as follows:
• RGB (Hex): #C75B12
• PantoneĀ® 159 C
• CMYK: 1 / 74 / 100 / 7
• ***MUST INCLUDE ALL INFORMATION THAT IS ON OUR CURRENT LETTERHEAD***
Should not have
• Please do not include the word 'contractors'

```html
<!DOCTYPE html>
<html lang="en">
<head>
<meta charset="utf-8">
<title>K&amp;W Stationery</title>
<link href="https://fonts.googleapis.com/css2?family=Arimo:wght@400;700&display=swap" rel="stylesheet">
<style>
  :root{
    --bg:#dfe0df;
    --paper:#ffffff;
    --navy:#13204a;
    --ochre:#e8602a;
    --ink:#2b2b2b;
    --muted:#555;
  }
  *{box-sizing:border-box;margin:0;padding:0}
  html,body{width:1200px;height:1000px;overflow:hidden}
  body{background:var(--bg);font-family:"Arimo",Arial,sans-serif;color:var(--ink);position:relative}
  .sheet{position:absolute;background:var(--paper);box-shadow:0 8px 6px -6px rgba(0,0,0,.25)}
  .strip{position:absolute;right:0;top:0;bottom:0;background:var(--navy)}
  .strip .accent{position:absolute;left:0;right:0;bottom:0;background:var(--ochre)}
  .brand{position:absolute;font-weight:700;color:var(--navy);line-height:1;white-space:nowrap}
  .brand.light{color:#fff}
  .contact{position:absolute;font-size:5px;line-height:7px;color:var(--ink);white-space:nowrap}
  .contact .row{display:flex;align-items:center;gap:3px}
  .dot{width:5px;height:5px;border-radius:50%;background:#333;display:inline-block;flex:none}
  .cols{position:absolute;display:flex;gap:12px}
  /* business card */
  .card-front{left:76px;top:163px;width:227px;height:130px}
  .card-back{left:335px;top:163px;width:227px;height:130px;background:var(--navy)}
  .person{position:absolute;left:236px;top:261px;font-size:6.5px;letter-spacing:.5px;text-align:right;width:42px}
  .person small{display:block;font-size:4.5px;letter-spacing:.8px}
  /* slip */
  .slip{left:55px;top:341px;width:551px;height:240px}
  /* envelope */
  .envelope{left:61px;top:615px;width:550px;height:240px}
  .flap{position:absolute;left:0;top:0;width:100%;height:83px;background:var(--navy);border-radius:0 0 20px 20px}
  /* letterhead */
  .letter{left:640px;top:138px;width:505px;height:714px}
  .letter-body{position:absolute;left:78px;top:166px;width:330px;font-size:11.3px;line-height:14.4px;color:#333}
  .letter-body p{text-align:justify;margin-bottom:14.4px}
  .signoff strong{display:block;font-weight:400;font-size:10.5px;letter-spacing:.3px;margin-top:0}
  .signoff span{font-size:9px}
</style>
</head>
<body>

<!-- Business card front -->
<div class="sheet card-front">
  <div class="brand" style="left:23px;top:19px;font-size:17px">K&amp;W</div>
  <div class="contact" style="left:18px;top:73px">
    <div class="row"><span class="dot"></span>42 Ridge St, Dune Flat</div>
    <div class="row" style="padding-left:8px">NT 0870 . PO Box 512</div>
    <div class="row"><span class="dot"></span>08 5550 123</div>
    <div class="row"><span class="dot"></span>0400 555 123</div>
    <div class="row"><span class="dot"></span>0805550 123</div>
    <div class="row"><span class="dot"></span>info@kwgroup.com.au</div>
    <div class="row"><span class="dot"></span>www.kwgroup.com.au</div>
  </div>
  <div class="strip" style="width:8px"><div class="accent" style="height:33px"></div></div>
</div>
<div class="person">YOUR NAME<small>POSITION</small></div>

<!-- Business card back -->
<div class="sheet card-back">
  <div class="brand light" style="left:85px;top:52px;font-size:29px">K&amp;W</div>
  <div class="strip" style="width:9px;background:transparent"><div class="accent" style="height:33px"></div></div>
</div>

<!-- Compliment slip -->
<div class="sheet slip">
  <div class="brand" style="left:415px;top:45px;font-size:26px">K&amp;W</div>
  <div class="cols" style="left:42px;top:202px">
    <div class="contact" style="position:static">
      <div class="row"><span class="dot"></span>42 Ridge St, Dune Flat</div>
      <div class="row" style="padding-left:8px">NT 0870 . PO Box 512</div>
    </div>
    <div class="contact" style="position:static;margin-left:20px">
      <div class="row"><span class="dot"></span>08 5550 123</div>
      <div class="row"><span class="dot"></span>0805550 123</div>
    </div>
    <div class="contact" style="position:static">
      <div class="row"><span class="dot"></span>info@kwgroup.com.au</div>
      <div class="row"><span class="dot"></span>www.kwgroup.com.au</div>
    </div>
  </div>
  <div class="strip" style="width:12px"><div class="accent" style="height:58px"></div></div>
</div>

<!-- Envelope -->
<div class="sheet envelope">
  <div class="flap">
    <div class="brand light" style="left:246px;top:26px;font-size:26px">K&amp;W</div>
  </div>
</div>

<!-- Letterhead -->
<div class="sheet letter">
  <div class="brand" style="left:219px;top:68px;font-size:29px">K&amp;W</div>
  <div class="letter-body">
    <p style="margin-bottom:10px">Dear Sir/Madam</p>
    <p>Lorem ipsum dolor sit amet, mel dicta signiferumque in, duo in summo albucius, vide idque eos id. Eos eu aperiri omittam. Hinc percipit omittantur pri et, in cum minimum vituperata. Dolor libris no sit, eum id porro tritani disputando, usu mutat dolore interesset ad.</p>
    <p>Zril tacimates splendide vim ex, ut falli docendi pro. At ubique pericula mei. Te exerci voluptatum sit, vix at esse ullum scaevola, iusto sonet urbanitas vim ad. No mea ornatus veritus. At est assum fastidii, quo id noluisse phaedrum, mea ea oblique facilisi.</p>
    <p>Sed eu discere delicatissimi, quo probo gloriatur cu, cu est mollis voluptua. No atqui discere saperet quo. Laudem facilisi patrioque ut vim, ut unum aperiam invenire quo, eu sonet veritus corpora qui. Ludus posidonium quo at. Eam ei liber detraxit.</p>
    <p>Ex officiis honestatis usu. Pro regione patrioque similique eu. Animal noluisse et quo, blandit voluptua molestiae eu duo, eos et labore labores. Ea recusabo quaestio suavitate duo.</p>
    <p>Duo alienum efficiantur ea, et sea autem aliquando. Ei eam wisi inani offendit, tibique erroribus voluptatibus in sit. Altera essent latine in cum, eum an doctus dissentias. Te mea latine copiosae percipitur, vix te docendi singulis gloriatur. Ex omnium inermis gloriatur his, impetus tamquam quo an. Ut has aeterno mandamus.</p>
    <div class="signoff"><strong>JOHN DOE</strong><span>President</span></div>
  </div>
  <div class="cols" style="left:37px;top:667px">
    <div class="contact" style="position:static">
      <div class="row"><span class="dot"></span>42 Ridge St, Dune Flat</div>
      <div class="row" style="padding-left:8px">NT 0870 . PO Box 512</div>
    </div>
    <div class="contact" style="position:static">
      <div class="row"><span class="dot"></span>08 5550 123</div>
      <div class="row"><span class="dot"></span>0805550 123</div>
    </div>
    <div class="contact" style="position:static">
      <div class="row"><span class="dot"></span>info@kwgroup.com.au</div>
      <div class="row"><span class="dot"></span>www.kwgroup.com.au</div>
    </div>
  </div>
  <div class="strip" style="width:14px"><div class="accent" style="height:84px"></div></div>
</div>

</body>
</html>
```